Design my dad a new business card because his current one sucks!

I need a business card designed for my fathers home maintenance business. His customers are individuals (single moms, old people etc.) as well as the occasional business. As such it needs to be accessible to both target audiences.

The front of the card should be dark grey on yellow with the logo and contain the following information:
- Warren Dobrinski
- 0487 362 914
- info@harbourlinehandyworks.com.au
- 0487 362 914

- ABN: 87 214 630 592
- 'Fully Insured'

The reverse should be yellow on dark grey and will have the web address:
- harbourlinehandyworks.com.au

And a few key services he offers:
GENERAL REPAIRS
PAINTING/TILING/
PAVING &CONCRETING
PRESSURE WASHING
ON-SITE WELDING
DECKING ADDITIONS & REPAIRS
FENCING
FULL BOND CLEANING

This will be first time the logo has been printed so you will need to come up with the best CMYK approximation of the RGB colours to make sure it is a close as possible.

```html
<!DOCTYPE html>
<html lang="en">
<head>
<meta charset="utf-8">
<title>Harbourline Handyworks – Business Card</title>
<link rel="stylesheet" href="https://fonts.googleapis.com/css2?family=Open+Sans:wght@400;600;700&family=Roboto+Condensed:wght@400&display=swap">
<style>
  :root {
    --yellow: #f6d21a;
    --yellow-deep: #f2c30c;
    --charcoal: #3a3a3c;
    --charcoal-dark: #2b2b2d;
    --ink: #3d3d3d;
    --backdrop: #e9e5df;
  }
  * { box-sizing: border-box; margin: 0; padding: 0; }
  html, body {
    width: 1200px; height: 913px; overflow: hidden;
    background: var(--backdrop);
  }
  .stage {
    width: 1200px; height: 913px;
    display: flex; align-items: center; justify-content: center; gap: 56px;
  }
  .card {
    position: relative;
    width: 520px; height: 318px;
    border-radius: 4px;
    box-shadow: 0 10px 28px rgba(0,0,0,0.22);
    overflow: hidden;
  }
  /* Front */
  .card--front {
    background: linear-gradient(160deg, var(--yellow) 0%, var(--yellow-deep) 100%);
    color: var(--ink);
    font-family: "Open Sans", sans-serif;
  }
  .brand {
    position: absolute;
    display: flex; align-items: center; gap: 10px;
    font-family: "Open Sans", sans-serif;
    font-weight: 700;
  }
  .brand__mark {
    width: 26px; height: 26px; border-radius: 50%;
    flex: none;
  }
  .brand__name { line-height: 1.05; letter-spacing: -0.3px; }
  .card--front .brand { top: 30px; right: 32px; color: var(--ink); font-size: 25px; }
  .card--front .brand__mark { background: var(--ink); }
  .holder { position: absolute; left: 36px; top: 132px; }
  .holder__name { font-size: 21px; font-weight: 400; }
  .holder__role { font-size: 12px; font-weight: 600; margin-top: 2px; }
  .details { position: absolute; left: 36px; bottom: 30px; }
  .details__insured { font-size: 20px; font-weight: 400; margin-bottom: 8px; }
  .details__line { font-size: 12.5px; line-height: 1.6; }
  .details__line b { font-weight: 700; }

  /* Back */
  .card--back {
    background: linear-gradient(160deg, var(--charcoal) 0%, var(--charcoal-dark) 100%);
    color: var(--yellow);
  }
  .card--back .brand {
    top: 40px; left: 0; right: 0; justify-content: center;
    font-size: 30px; color: var(--yellow);
  }
  .card--back .brand__mark { background: var(--yellow); width: 30px; height: 30px; }
  .services {
    position: absolute; top: 150px; left: 0; right: 0;
    list-style: none; text-align: center;
    font-family: "Roboto Condensed", sans-serif;
    font-size: 15px; letter-spacing: 0.4px; line-height: 1.65;
  }
  .services li { display: inline; }
  .services .dot { margin: 0 6px; }
  .web {
    position: absolute; bottom: 34px; left: 0; right: 0; text-align: center;
    font-family: "Roboto Condensed", sans-serif;
    font-size: 19px; letter-spacing: 0.6px;
  }
</style>
</head>
<body>
<main class="stage">
  <section class="card card--front" aria-label="Card front">
    <div class="brand">
      <span class="brand__mark"></span>
      <span class="brand__name">Harbourline<br>Handyworks</span>
    </div>
    <div class="holder">
      <p class="holder__name">Warren Dobrinski</p>
      <p class="holder__role">owner</p>
    </div>
    <div class="details">
      <p class="details__insured">Fully Insured</p>
      <p class="details__line"><b>Ph:</b> 0487 362 914</p>
      <p class="details__line"><b>Email:</b> info@harbourlinehandyworks.com.au</p>
      <p class="details__line"><b>ABN:</b> 87 214 630 592</p>
    </div>
  </section>

  <section class="card card--back" aria-label="Card back">
    <div class="brand">
      <span class="brand__mark"></span>
      <span class="brand__name">Harbourline Handyworks</span>
    </div>
    <ul class="services">
      <li>GENERAL REPAIRS</li><span class="dot">•</span><li>PAINTING/TILING</li><span class="dot">•</span><li>PAVING &amp; CONCRETING</li><br>
      <li>PRESSURE WASHING</li><span class="dot">•</span><li>ON SITE WELDING</li><span class="dot">•</span><li>DECKING ADDITIONS &amp; REPAIRS</li><br>
      <li>FENCING</li><span class="dot">•</span><li>FULL BOND CLEANING</li>
    </ul>
    <p class="web">www.harbourlinehandyworks.com.au</p>
  </section>
</main>
</body>
</html>
```